Kellow Family Law, legal technician needs a website and design

I need a website for a family law practice. I specialize in collaborative law, unbundled services, and mediation. The website must contain my company logo (file attached), and the website must be a mixture of my personality and my profession. I have attached additional information to explain my personality and profession.

Target Market(s)

Lower through middle-class (income level up to $200,000 per year)

Coding

Coded - Design and coding required

Number of Pages Required

1 page

Requirements
Must have
• Must have enough pages to cover required content. I submitted below some content about the collaborative law process. All of the content is not necessary. However, the website must have enough content to clearly describe the services I offer. Use your professionalism and judgment regarding font, font size, etc.

```html
<!DOCTYPE html>
<html lang="en">
<head>
<meta charset="utf-8">
<title>Kellow Family Law</title>
<link rel="stylesheet" href="https://fonts.googleapis.com/css2?family=Cinzel:wght@400;600&family=Lora:wght@400;600&display=swap">
<style>
:root{
  --gold:#c8bd40;
  --gold-deep:#928437;
  --ink:#111111;
  --dark:#1b1b1b;
  --brown:#3b321b;
  --text:#444444;
  --muted:#777777;
  --light:#efefef;
  --white:#ffffff;
}
*{box-sizing:border-box;margin:0;padding:0}
html,body{width:1200px;height:2876px;overflow:hidden}
body{font-family:"Lora",Georgia,serif;color:var(--text);background:var(--white);position:relative}
.head{font-family:"Cinzel",Georgia,serif;font-weight:400;letter-spacing:1px}
.abs{position:absolute}
.btn{font-family:"Cinzel",Georgia,serif;display:flex;align-items:center;justify-content:center;letter-spacing:.5px}

/* hero */
.hero{position:absolute;left:0;top:0;width:1200px;height:518px;background:radial-gradient(ellipse at 60% 40%,#5a4a38 0%,#33291f 45%,#18130e 100%)}
.hero::after{content:"";position:absolute;inset:0;background:rgba(20,15,8,.35)}
.hero *{z-index:1}
.brand{left:98px;top:22px;display:flex;align-items:center;gap:12px}
.brand-mark{width:44px;height:44px;background:var(--gold)}
.brand-name{font-family:"Cinzel",serif;color:var(--white);font-size:20px;line-height:1.05;letter-spacing:1px}
.nav{left:384px;top:37px;display:flex;gap:28px;font-family:"Cinzel",serif;font-size:12px;color:var(--white)}
.nav .on{color:var(--gold);border-bottom:1px solid var(--gold);padding-bottom:4px}
.phone{left:970px;top:19px;color:var(--white);font-size:12px;display:flex;align-items:center;gap:5px}
.book{left:926px;top:44px;width:176px;height:27px;background:var(--gold);color:var(--ink);font-size:12px}
.hero-title{left:0;width:1200px;top:216px;text-align:center;color:var(--gold);font-size:40px;font-weight:600}
.hero-sub{left:0;width:1200px;top:265px;text-align:center;color:var(--white);font-family:"Cinzel",serif;font-size:13.5px;line-height:18px;font-weight:600}
.hero-btn{left:506px;top:318px;width:189px;height:32px;border:1px solid var(--gold);color:var(--gold);font-size:12px}

/* about */
.about-mark{left:150px;top:590px;width:355px;height:355px;display:flex;flex-direction:column;align-items:center;justify-content:center;gap:18px}
.about-mark .sq{width:90px;height:90px;background:var(--gold)}
.about-mark .nm{font-family:"Cinzel",serif;color:var(--gold-deep);font-size:34px;text-align:center;line-height:1.15}
.about-title{left:590px;top:618px;font-size:30px;color:var(--ink)}
.about-text{left:590px;top:680px;width:500px;font-size:12px;line-height:19.5px;color:var(--text)}
.about-text p+p{margin-top:35px}
.about-btn{left:590px;top:889px;width:115px;height:31px;border:1px solid var(--ink);color:var(--ink);font-size:12px;border-radius:2px}

/* practice */
.practice{position:absolute;left:0;top:1020px;width:1200px;height:424px;background:linear-gradient(180deg,#3e341b,#2c2513 60%,#3a3019)}
.sec-title{left:0;width:1200px;text-align:center;font-size:30px}
.p-card{top:141px;width:320px;height:191px}
.p-photo1{background:linear-gradient(135deg,#5b6470,#2f343b 60%,#8a8f96)}
.p-photo2{background:linear-gradient(135deg,#b9b5ad,#6f6c67 55%,#d0ccc4)}
.p-mid{background:linear-gradient(180deg,#1a1a1a,#0b0b0b);text-align:center;padding:38px 34px 0}
.p-mid h3{font-family:"Cinzel",serif;font-weight:400;color:var(--gold);font-size:18px;letter-spacing:1px;margin-bottom:12px}
.p-mid p{color:var(--white);font-size:13.5px;line-height:18px}
.p-label{top:315px;width:218px;height:33px;background:var(--gold);color:var(--ink);font-size:14px}

/* prices */
.plan{top:1577px;width:320px;height:398px;background:var(--white);box-shadow:0 2px 10px rgba(0,0,0,.1)}
.plan-head{height:93px;display:flex;align-items:center;justify-content:center;text-align:center;font-family:"Cinzel",serif;font-size:16px;line-height:18px;color:var(--ink);padding:0 30px;letter-spacing:1px}
.plan-price{height:77px;background:linear-gradient(90deg,#0c0c0c,#2a2a2a 50%,#0c0c0c);display:flex;justify-content:center;gap:45px;color:var(--white);text-align:center;padding-top:10px}
.plan-price b{display:block;font-family:"Lora",serif;font-size:36px;line-height:40px;font-weight:600}
.plan-price small{display:block;font-size:10px;line-height:11px}
.plan ul{list-style:none;padding:32px 30px 0 31px;font-size:11.5px;line-height:12px;color:var(--muted)}
.plan li{margin-bottom:8px}
.plan li::before{content:"\25B8";font-size:9px;margin-right:6px}
.plan-btn{position:absolute;left:8px;bottom:8px;width:304px;height:37px;background:var(--light);color:var(--ink);font-size:12px}
.plan.feat{background:var(--gold)}
.plan.feat ul{color:var(--ink)}
.plan.feat .plan-btn{background:var(--ink);color:var(--white)}

/* blogs */
.blogs{position:absolute;left:0;top:2066px;width:1200px;height:435px;background:linear-gradient(180deg,#e6e6e6,#f2f2f2 50%,#e1e1e1)}
.post{top:134px;width:491px;height:167px;background:var(--white)}
.date{left:7px;top:8px;width:75px;height:79px;background:var(--gold);color:var(--ink);text-align:center;padding-top:14px}
.date b{display:block;font-family:"Lora",serif;font-weight:400;font-size:32px;line-height:32px}
.date span{font-family:"Cinzel",serif;font-size:11px}
.post h4{position:absolute;left:104px;top:18px;width:340px;font-family:"Cinzel",serif;font-weight:400;font-size:16px;line-height:20px;color:var(--ink);letter-spacing:1px}
.post p{position:absolute;left:104px;top:66px;width:350px;font-size:12px;line-height:17px;color:var(--muted)}
.post .rm{position:absolute;left:104px;top:116px;width:106px;height:26px;border:1px solid #999;color:var(--ink);font-size:10px}
.view{left:551px;top:337px;width:98px;height:29px;background:var(--gold);color:var(--ink);font-size:12px}

/* footer */
.footer{position:absolute;left:0;top:2501px;width:1200px;height:338px;background:var(--ink);color:var(--white)}
.f-brand{left:98px;top:75px;display:flex;flex-direction:column;gap:10px}
.f-brand .sq{width:46px;height:46px;background:var(--gold)}
.f-brand .nm{font-family:"Cinzel",serif;color:var(--gold);font-size:17px;line-height:20px}
.f-h{top:73px;font-family:"Cinzel",serif;color:var(--gold-deep);font-size:17px;letter-spacing:.5px;font-weight:400}
.f-links{left:262px;top:113px;list-style:none;font-size:12px;line-height:26px}
.f-links .on{color:var(--gold-deep);text-decoration:underline}
.f-label{font-family:"Cinzel",serif;font-size:11px;color:var(--gold-deep)}
.f-contact{left:421px;top:117px;font-size:12px;line-height:19px}
.f-contact .row{display:flex;align-items:center;gap:8px}
.field{width:220px;height:31px;border:1px solid #333;display:flex;align-items:center;gap:8px;padding-left:12px;font-size:11px;color:#aaa}
.comments{left:883px;top:119px;width:219px;height:116px;border:1px solid #333;padding:10px 12px;font-size:11px;color:#aaa;display:flex;gap:8px;align-items:flex-start}
.submit{left:649px;top:251px;width:92px;height:28px;background:var(--gold);color:var(--ink);font-family:"Lora",serif;font-size:11px;font-weight:600}
.bar{position:absolute;left:0;top:2839px;width:1200px;height:37px;background:var(--gold-deep);color:var(--white);font-size:11px}
.bar .copy{left:98px;top:12px}
.social{left:1018px;top:13px;display:flex;gap:12px}
.social span{width:11px;height:11px;background:var(--white);border-radius:50%}
</style>
</head>
<body>

<header class="hero" role="img" aria-label="Photo of a smiling family with a lawyer, dimmed behind the headline">
  <div class="abs brand"><div class="brand-mark"></div><div class="brand-name">Kellow<br>Family Law</div></div>
  <nav class="abs nav"><span class="on">Home</span><span>About Us</span><span>Practice Areas</span><span>Prices</span><span>Blogs</span><span>Contact Us</span></nav>
  <div class="abs phone"><svg width="8" height="11" viewBox="0 0 8 11"><rect x="0.5" y="0.5" width="7" height="10" rx="1" fill="none" stroke="#c8bd40"/></svg>555.014.2290</div>
  <div class="abs btn book">Book an Appointment</div>
  <h1 class="abs head hero-title">We Fight for You</h1>
  <p class="abs hero-sub">At Alder Law Group, justice is not an abstract term. It's something<br>we create everyday for our clients.</p>
  <div class="abs btn hero-btn">Contact us Today!</div>
</header>

<section>
  <div class="abs about-mark"><div class="sq"></div><div class="nm">Kellow<br>Family Law</div></div>
  <h2 class="abs head about-title">About Us</h2>
  <div class="abs about-text">
    <p>Lorem Ipsum is simply dummy text of the printing and typesetting industry. Lorem Ipsum has been the industry's standard dummy text ever since the 1500s, when an unknown printer took a galley of type and scrambled it to make a type specimen book...</p>
    <p>It has survived not only five centuries, but also the leap into electronic typesetting, remaining essentially unchanged. It was popularised in the 1960s with the release of Veltrane sheets containing Lorem Ipsum passages, and more recently with desktop publishing software like Quillset Studio including versions of Lorem Ipsum...</p>
  </div>
  <div class="abs btn about-btn">Read More</div>
</section>

<section class="practice">
  <h2 class="abs head sec-title" style="top:67px;color:var(--white)">Practice Areas</h2>
  <div class="abs p-card p-photo1" style="left:98px" role="img" aria-label="Photo of a team reviewing documents around a table"></div>
  <div class="abs p-card p-mid" style="left:440px"><h3>Unbundled Services</h3><p>Lawyer and client contract for specific and limited legal services without the lawyer being responsible for the whole case, i.e. a parenting plan.</p></div>
  <div class="abs p-card p-photo2" style="left:782px" role="img" aria-label="Photo of a couple in a mediation session"></div>
  <div class="abs btn p-label" style="left:149px">Collaborative Law</div>
  <div class="abs btn p-label" style="left:833px">Mediation</div>
</section>

<h2 class="abs head sec-title" style="top:1510px;color:var(--ink)">Prices</h2>

<div class="abs plan" style="left:98px">
  <div class="plan-head">Divorce without court services and fees</div>
  <div class="plan-price"><div><b>$899</b><small>plus court filing fee</small></div></div>
  <ul>
    <li>You've talked and you both agree on exactly what you want to do with your assets</li>
    <li>There is no need for mediation</li>
    <li>You have no children, or your children are older than 18</li>
    <li>Settlement Agreement is for tax purposes only</li>
    <li>Never go to court</li>
  </ul>
  <div class="btn plan-btn">Choose Plan</div>
</div>
<div class="abs plan" style="left:440px">
  <div class="plan-head">Settlement Agreement, Child Support, and Divorce Paperwork</div>
  <div class="plan-price"><div><b>$1,499</b><small>plus court filing fee</small></div></div>
  <ul>
    <li>You've talked and you both agree on exactly what you want to do your assets, your child support payments, divided expenses, and your payment time</li>
    <li>There's no need for mediation</li>
    <li>Never go to court</li>
  </ul>
  <div class="btn plan-btn">Choose Plan</div>
</div>
<div class="abs plan feat" style="left:782px">
  <div class="plan-head">Comprehensive Settlement Agreement and Divorce Paperwork</div>
  <div class="plan-price"><div><b>$1,898</b><small>plus court filing fee<br>no children</small></div><div><b>$2,937</b><small>plus court filing fee<br>with children</small></div></div>
  <ul>
    <li>You need neutral advice to settle on an asset/debt division, buyout for real property, or other issues</li>
    <li>Settlement Agreement is a Final Order for the court</li>
    <li>Settlement Agreement my include all child support, Parenting Plan, division of assets, and all othe issues to be settled</li>
    <li>Never go to court</li>
  </ul>
  <div class="btn plan-btn">Choose Plan</div>
</div>

<section class="blogs" role="img" aria-label="Faded photo of a family in the background">
  <h2 class="abs head sec-title" style="top:71px;color:var(--ink)">Blogs</h2>
  <article class="abs post" style="left:98px">
    <div class="abs date"><b>21</b><span>Jun. 21</span></div>
    <h4>Lorem Ipsum is simply dummy text of the printing</h4>
    <p>Lorem Ipsum has been the industry's standard dummy text ever since the 1500s, when an unknown...</p>
    <div class="btn rm">Read More</div>
  </article>
  <article class="abs post" style="left:611px">
    <div class="abs date"><b>18</b><span>Jun. 21</span></div>
    <h4>Lorem Ipsum is simply dummy text of the printing</h4>
    <p>Lorem Ipsum has been the industry's standard dummy text ever since the 1500s, when an unknown...</p>
    <div class="btn rm">Read More</div>
  </article>
  <div class="abs btn view">View All</div>
</section>

<footer class="footer">
  <div class="abs f-brand"><div class="sq"></div><div class="nm">Kellow<br>Family Law</div></div>
  <h5 class="abs f-h" style="left:262px">Quick Link</h5>
  <ul class="abs f-links"><li class="on">Home</li><li>About Us</li><li>Practice Areas</li><li>Prices</li><li>Blogs</li><li>Contact Us</li></ul>
  <h5 class="abs f-h" style="left:422px">Conatct Info</h5>
  <div class="abs f-contact">
    <div class="f-label">Call Us:</div>
    <div class="row" style="margin-top:6px"><svg width="11" height="11" viewBox="0 0 24 24"><path d="M6.6 10.8a15 15 0 0 0 6.6 6.6l2.2-2.2c.3-.3.7-.4 1-.2 1.1.4 2.3.6 3.6.6.6 0 1 .4 1 1V20c0 .6-.4 1-1 1A17 17 0 0 1 3 4c0-.6.4-1 1-1h3.5c.6 0 1 .4 1 1 0 1.3.2 2.5.6 3.6.1.3 0 .7-.2 1z" fill="#928437"/></svg>555 014 2291</div>
    <div class="row"><svg width="11" height="9" viewBox="0 0 11 9"><rect width="11" height="9" fill="#928437"/><path d="M0 0l5.5 5L11 0" stroke="#111" fill="none"/></svg>info@kellowfamilylaw.com</div>
    <div class="f-label" style="margin-top:20px">Address:</div>
    <div>48 Marlow Lane<br>Dover, NH 03820</div>
  </div>
  <h5 class="abs f-h" style="left:648px">Quick Inquiry</h5>
  <div class="abs field" style="left:648px;top:119px">&#9711; Name</div>
  <div class="abs field" style="left:648px;top:162px">&#9993; Email</div>
  <div class="abs field" style="left:648px;top:205px">&#9647; Phone</div>
  <div class="abs comments">&#9633; Comments</div>
  <div class="abs btn submit">Submit</div>
</footer>

<div class="bar">
  <div class="abs copy">Copyright &copy; 2021 Kellow Family Law. All Rights Reserved</div>
  <div class="abs social"><span></span><span></span><span></span><span></span></div>
</div>

</body>
</html>
```